Velmora Partners GAP Brochure Design Project

We are looking for a designer to create a point of sale brochure, the item will be used by Motor Dealers when they are selling our product to their customers, the product is an insurance product that covers the difference between the purchase price of the vehicle and the amount offered by the insurance company in the event the car is stolen or written off by the insurance company. Therefore we are look at a Business to Retail Customer relationship.
Please note we are in the process of designing a logo via ArtHarbor that will need to be used in the brochure. I have attached an example of a competitors POS. I am not concerned about including all of the terms and conditions and would prefer to keep the design as a two sided folded but obviously we will need some space for text. This is used by sales people as a sales aid.
Reason: The reference document did not upload, please let me know if you need further information.
Insurance

```html
<!DOCTYPE html>
<html lang="en">
<head>
<meta charset="utf-8">
<title>Velmora Partners – GAP Brochure</title>
<link href="https://fonts.googleapis.com/css2?family=Ubuntu:wght@400;500;700&display=swap" rel="stylesheet">
<style>
  :root {
    --stage: #2b2d2f;
    --blue-deep: #0b2a9e;
    --blue-mid: #1d4fd6;
    --blue-bright: #3d86ff;
    --ring: #9fd4ff;
    --grey-light: #f2f2f2;
    --grey-mid: #c9c9c9;
    --grey-dark: #8d8d8d;
    --band: #d6d6d6;
    --ink: #1f1f1f;
    --ink-soft: #555;
    --white: #ffffff;
  }
  * { box-sizing: border-box; margin: 0; padding: 0; }
  html, body {
    width: 1200px; height: 900px; overflow: hidden;
    background: var(--stage);
    font-family: "Ubuntu", Arial, sans-serif;
  }
  .spread {
    position: absolute; left: 25px; top: 181px;
    display: grid;
    grid-template-columns: 560px 560px;
    grid-template-rows: 254px 254px;
    gap: 30px;
  }
  .panel {
    position: relative; overflow: hidden;
    box-shadow: 0 2px 10px rgba(0,0,0,.5);
  }

  /* cover + back */
  .panel--blue {
    background: linear-gradient(120deg, var(--blue-deep) 0%, var(--blue-mid) 55%, var(--blue-bright) 100%);
  }
  .cover__photo {
    position: absolute; left: -50px; top: -73px;
    width: 400px; height: 400px; border-radius: 50%;
    background: radial-gradient(circle at 45% 55%, #d8dadc 0%, #6d7073 35%, #2a2c2e 70%, #111 100%);
  }
  .cover__ring {
    position: absolute; left: -44px; top: -79px;
    width: 412px; height: 412px; border-radius: 50%;
    border: 3px solid var(--ring); opacity: .55;
  }
  .brand { color: var(--white); text-align: right; }
  .brand__name { font-weight: 700; font-size: 14px; letter-spacing: .2px; }
  .brand__tag { font-size: 7px; margin-top: 1px; }
  .cover__brand { position: absolute; right: 72px; top: 158px; }

  .back { display: flex; flex-direction: column; align-items: center; justify-content: center; }
  .back__brand { text-align: center; margin-bottom: 16px; }
  .back__brand .brand__tag { text-align: right; }
  .back__contact {
    color: var(--white); font-size: 6.4px; line-height: 1.35; text-align: center;
  }

  /* inner pages */
  .panel--grey {
    background: radial-gradient(ellipse at 40% 50%, var(--grey-light) 0%, var(--grey-mid) 65%, var(--grey-dark) 100%);
  }
  .band {
    position: absolute; top: 34px; height: 22px;
    background: linear-gradient(90deg, rgba(214,214,214,.95), rgba(214,214,214,.6));
    color: var(--ink-soft); font-size: 14px; line-height: 22px;
  }
  .intro .band { left: 0; width: 228px; padding-left: 42px; }
  .claims .band { right: 0; width: 266px; padding-left: 18px; }
  .copy { position: absolute; color: var(--ink); font-size: 6.5px; line-height: 1.22; text-align: justify; }
  .intro .copy { left: 68px; top: 82px; width: 210px; }
  .claims .copy { left: 132px; top: 78px; width: 400px; }
  .claims .copy p + p { margin-top: 20px; }

  .intro__photo {
    position: absolute; right: 0; top: 0; width: 214px; height: 100%;
    background: linear-gradient(160deg, #f4c0c6 0%, #e2303c 30%, #b3121d 65%, #3a1010 100%);
  }
  .claims__photo {
    position: absolute; left: 0; top: 0; width: 112px; height: 100%;
    background: linear-gradient(180deg, #3a3b3d 0%, #6e7073 45%, #d9dadb 62%, #444 100%);
  }
</style>
</head>
<body>
<main class="spread">

  <section class="panel panel--blue cover">
    <div class="cover__photo" role="img" aria-label="Photograph of a dark grey sports coupe, front three-quarter view"></div>
    <div class="cover__ring"></div>
    <div class="brand cover__brand">
      <div class="brand__name">Velmora Partners</div>
      <div class="brand__tag">car insurance</div>
    </div>
  </section>

  <section class="panel panel--grey intro">
    <h2 class="band">introduction / welcome</h2>
    <div class="copy">
      <p>Welcome to Asset Protection from Carvault. This policy is designed to help you in the event that your vehicle is stolen or damaged beyond economical repair and deemed to be a total loss by your motor insurance company.<br>
      Should the worst happen, Carvault Asset Protection will pay the difference between the write off settlement from your motor insurance company and the price your paid for your vehicle or the outstanding balance on your vehicle finance agreement, whichever is greater.<br>
      We hope you never need to claim on your Carvault Asset Protection but if you do, you should follow the claims process.<br>
      Please keep this book safe as you will need it if you have to make a claim – please don't store it in your vehicle, we recommend keeping it with your motor insurance documents. Carvault Asset Protection provides an exceptionally high level of cover and has received the top 5-star rating by Ratewise, the UK's leading independent financial services rating agency.</p>
    </div>
    <div class="intro__photo" role="img" aria-label="Photograph of the rear of a red hatchback with spoiler and tail light"></div>
  </section>

  <section class="panel panel--grey claims">
    <div class="claims__photo" role="img" aria-label="Photograph of a white sports coupe in a dark studio"></div>
    <h2 class="band">claims / conditions &amp; exceptions</h2>
    <div class="copy">
      <p>Welcome to Asset Protection from Carvault. This policy is designed to help you in the event that your vehicle is stolen or damaged beyond economical repair and deemed to be a total loss by your motor insurance company.<br>
      Should the worst happen, Carvault Asset Protection will pay the difference between the write off settlement from your motor insurance company and the price your paid for your vehicle or the outstanding balance on your vehicle finance agreement, whichever is greater.</p>
      <p>Welcome to Asset Protection from Carvault. This policy is designed to help you in the event that your vehicle is stolen or damaged beyond economical repair and deemed to be a total loss by your motor insurance company.<br>
      Should the worst happen, Carvault Asset Protection will pay the difference between the write off settlement from your motor insurance company and the price your paid for your vehicle or the outstanding balance on your vehicle finance agreement, whichever is greater.</p>
      <p>Welcome to Asset Protection from Carvault. This policy is designed to help you in the event that your vehicle is stolen or damaged beyond economical repair and deemed to be a total loss by your motor insurance company.<br>
      Should the worst happen, Carvault Asset Protection will pay the difference between the write off settlement from your motor insurance company and the price your paid for your vehicle or the outstanding balance on your vehicle finance agreement, whichever is greater.</p>
    </div>
  </section>

  <section class="panel panel--blue back">
    <div class="brand back__brand">
      <div class="brand__name">Velmora Partners</div>
      <div class="brand__tag">car insurance</div>
    </div>
    <address class="back__contact" style="font-style:normal">
      Carvault Asset Protection is administered by Motorshield Plan Limited.<br>
      Motorshield Plan, Harbour Court, 12 Eastgate Trading Estate,<br>
      Millbrook, North Riding MB4 2LQ<br>
      www.motorshieldplan.co.uk<br>
      Phone: 0800 410 2275 Fax: 0800 410 2276
    </address>
  </section>

</main>
</body>
</html>
```